Heritage Depot Business Cards

Require a business card design. <br/><br/>Needs to include logo (either round or long version) plus these details:<br/>Maya Corvell<br/>Heritage Depot<br/>maya@brightmarttrade.com.au<br/>02 6418 7395<br/>PO Box Glenfarrow NSW 2791<br/>www.heritagedepot.com.au<br/><br/>I need in an editable format so that I can create for multiple staff members. <br/><br/>

Target Market(s)

We are an online store selling renovation products to home owners are builders. Looking for a classic classy design.

Industry/Entity Type

Home And Garden

Contact Information for Business Card

Maya Corvell
Heritage Depot
maya@brightmarttrade.com.au
02 6418 7395
PO Box Glenfarrow NSW 2791
www.heritagedepot.com.au

Colors

Designer to choose colors to be used in the design.

Requirements
Must have
• Must include Logo.

```html
<!DOCTYPE html>
<html lang="en">
<head>
<meta charset="utf-8">
<title>Heritage Depot Business Cards</title>
<link href="https://fonts.googleapis.com/css2?family=Poppins:wght@300;400;500;700&display=swap" rel="stylesheet">
<style>
  :root {
    --page-bg: #d9d9d9;
    --card-white: #ffffff;
    --card-dark: #2c2929;
    --ink: #1f1d1d;
    --ink-soft: #3a3737;
    --paper-text: #ffffff;
    --sketch-light: #e9e9e9;
    --sketch-dark: #3a3636;
  }
  * { box-sizing: border-box; margin: 0; padding: 0; }
  html, body { width: 1200px; height: 900px; overflow: hidden; }
  body {
    background: var(--page-bg);
    font-family: "Poppins", sans-serif;
    display: flex;
    flex-direction: column;
    align-items: center;
    justify-content: center;
    gap: 40px;
  }
  .card {
    width: 630px;
    height: 360px;
    position: relative;
    overflow: hidden;
    box-shadow: 0 6px 18px rgba(0,0,0,0.18);
  }

  /* Front */
  .card-front {
    background: var(--card-white);
    color: var(--ink);
  }
  .brand {
    position: absolute;
    left: 70px;
    top: 110px;
    display: flex;
    align-items: center;
    gap: 16px;
  }
  .brand-dot {
    width: 44px;
    height: 44px;
    border: 2px solid var(--ink);
    border-radius: 50%;
  }
  .brand-name {
    font-weight: 500;
    font-size: 52px;
    letter-spacing: 0.5px;
    color: var(--ink);
    line-height: 1;
  }
  .front-url {
    position: absolute;
    left: 100px;
    top: 230px;
    font-size: 22px;
    font-weight: 500;
    color: var(--ink-soft);
    letter-spacing: 0.3px;
  }

  /* Back */
  .card-back {
    background: var(--card-dark);
    color: var(--paper-text);
  }
  .holder {
    position: absolute;
    left: 46px;
    top: 30px;
  }
  .holder-name {
    font-weight: 700;
    font-size: 22px;
    line-height: 1.2;
  }
  .holder-company {
    font-weight: 300;
    font-size: 15px;
    margin-top: 2px;
  }
  .contact-list {
    position: absolute;
    left: 46px;
    top: 104px;
    list-style: none;
    display: flex;
    flex-direction: column;
    gap: 9px;
  }
  .contact-item {
    display: flex;
    align-items: flex-start;
    gap: 12px;
    font-weight: 300;
    font-size: 15px;
    line-height: 22px;
  }
  .contact-icon {
    width: 22px;
    height: 22px;
    flex: none;
  }
  .roof-sketch {
    position: absolute;
    left: 150px;
    top: 232px;
    width: 480px;
    height: 128px;
    background: linear-gradient(160deg, var(--sketch-light) 0%, #9a9797 55%, var(--sketch-dark) 100%);
    clip-path: polygon(0 12%, 100% 0, 100% 100%, 22% 100%);
    opacity: 0.85;
  }
</style>
</head>
<body>

  <section class="card card-front" aria-label="Business card front">
    <div class="brand">
      <span class="brand-dot"></span>
      <span class="brand-name">Heritage Depot</span>
    </div>
    <p class="front-url">www.heritagedepot.com.au</p>
  </section>

  <section class="card card-back" aria-label="Business card back">
    <div class="holder">
      <h1 class="holder-name">Maya Corvell</h1>
      <p class="holder-company">Heritage Depot</p>
    </div>

    <ul class="contact-list">
      <li class="contact-item">
        <svg class="contact-icon" viewBox="0 0 22 22" aria-hidden="true">
          <circle cx="11" cy="11" r="10" fill="none" stroke="#fff" stroke-width="1.3"/>
          <path d="M8 6.5c-.8.6-1 1.6-.5 2.8.9 2.2 2.5 3.9 4.6 4.9 1.2.5 2.2.3 2.8-.5l-1.6-1.5-1.2.6c-1.1-.6-1.9-1.4-2.5-2.5l.6-1.2z" fill="#fff"/>
        </svg>
        <span>02 6418 7395</span>
      </li>
      <li class="contact-item">
        <svg class="contact-icon" viewBox="0 0 22 22" aria-hidden="true">
          <circle cx="11" cy="11" r="10" fill="none" stroke="#fff" stroke-width="1.3"/>
          <rect x="6" y="7.5" width="10" height="7" fill="none" stroke="#fff" stroke-width="1.2"/>
          <path d="M6 7.5l5 4 5-4" fill="none" stroke="#fff" stroke-width="1.2"/>
        </svg>
        <span>maya@brightmarttrade.com.au</span>
      </li>
      <li class="contact-item">
        <svg class="contact-icon" viewBox="0 0 22 22" aria-hidden="true">
          <circle cx="11" cy="11" r="10" fill="none" stroke="#fff" stroke-width="1.3"/>
          <circle cx="11" cy="11" r="5.5" fill="none" stroke="#fff" stroke-width="1.1"/>
          <ellipse cx="11" cy="11" rx="2.3" ry="5.5" fill="none" stroke="#fff" stroke-width="1"/>
          <path d="M5.5 11h11M6.3 8.3h9.4M6.3 13.7h9.4" stroke="#fff" stroke-width="0.9"/>
        </svg>
        <span>www.heritagedepot.com.au</span>
      </li>
      <li class="contact-item">
        <svg class="contact-icon" viewBox="0 0 22 22" aria-hidden="true">
          <circle cx="11" cy="11" r="10" fill="none" stroke="#fff" stroke-width="1.3"/>
          <path d="M11 16.5s-4-4.2-4-7a4 4 0 0 1 8 0c0 2.8-4 7-4 7z" fill="none" stroke="#fff" stroke-width="1.2"/>
          <circle cx="11" cy="9.5" r="1.4" fill="#fff"/>
        </svg>
        <span>PO Box Glenfarrow<br>NSW 2791</span>
      </li>
    </ul>

    <div class="roof-sketch" role="img" aria-label="Hand-drawn chalk sketch of a roof gable with hatched triangular panels"></div>
  </section>

</body>
</html>
```